Gulf Powerfair Infographic

We need to have an Infographic designed that displays statistics about the energy sector in Saudi Arabia.

We are an exhibitions organiser but we only want to link it back to the exhibition, Gulf Powerfair, by including our logo in the corner under the title 'Created by' (the logo is attached). The rest of the information and design needs to be entirely related to the industry and not the exhibition at all.

The objective of the Infographic is to convey the hard facts about a serious topic in an easy to digest manner. I have attached a word document with a few Infographic designs that we like.

We are using the Infographic for digital designs only so please make sure the Infographic fits onto a web screen easily and there is no need to scroll to see the information but other than that we are relatively flexible on the size.

The content is as follows but please feel free to interpret the content rather than copy word for word:
- Electricity consumption in Saudi Arabia increased sharply during the 1990–2010 period due to rapid economic development. Peak loads reached nearly 24 GW in 2001—25 times their 1975 level-and are expected to approach 60 GW by 2023
- The investment needed to meet this demand may exceed $90 billion. Consequently, there is an urgent need to develop energy conservation policies for sustainable development
- Generation capacity is approximately 55 GW. A looming energy shortage requires Saudi Arabia to increase its capacity. Capacity is planned to be increased to 120 GW by 2020.
- The government has approved the construction of a $300 million facility to turn waste into energy. The facility will process 180 tons of waste per day, producing 6 MW of electricity and 250,000 US gallons (950 m3) of distilled water.
- If energy conservation is successful, demand can be reduced by 5–10%. This is equivalent to 3–6 GW of additional capacity, which represents a possible $1.5–3.0 billion saving over 20 years.
- Saudi Arabia, has said it hopes to generate solar power of up to 41GW by 2032, or 30 per cent of peak power demand. That is almost double the current capacity of Germany, the world’s leading solar power.
- Saudi Arabia will invest in 17 new nuclear reactors in next 20 years.
- Coastal Brine Treatment Authority needs to increase desalinated water supply to 8.5m cubic metres a day by 2025
- Saudi Arabia is building the world’s largest solar-powered desalination plant at Khafji, which will produce 30,000 cubic metres a day of water once it is completed in the next two years. All power and water plants built from 2020 onwards will run on solar energy, NOVRA’s Prince Halvan said.
- Construction projects worth $75.6bn in Saudi Arabia during 2014, over 10% increase from 2013, $195.4 billion worth of construction planned in Saudi Arabia in the coming three years, and a further over $1 trillion worth of projects planned or under construction

Feel free to post any questions about this project and I will get back to you as soon as possible.

I look forward to seeing your designs!

```html
<!DOCTYPE html>
<html lang="en">
<head>
<meta charset="utf-8">
<title>Energy in Saudi Arabia — Infographic</title>
<link href="https://fonts.googleapis.com/css2?family=Oswald:wght@400;500;600&family=Nunito:wght@300;400;600;800&display=swap" rel="stylesheet">
<style>
:root{
  --cream:#fbf7dc;
  --green-pale:#e8eeb4;
  --teal:#1f5e7f;
  --navy:#283a8c;
  --orange:#f07a2a;
  --orange-deep:#e8631f;
  --yellow:#f8ee7c;
  --yellow-soft:#fbf3a4;
  --title-green:#2d7b3c;
  --ink:#223366;
  --white:#ffffff;
}
*{box-sizing:border-box}
html,body{margin:0;padding:0;overflow:hidden;background:var(--cream)}
.canvas{position:relative;width:1081px;height:1200px;overflow:hidden;background:var(--cream);font-family:"Nunito",sans-serif;color:var(--ink)}
.canvas > *{position:absolute;margin:0}
.cond{font-family:"Oswald",sans-serif;font-weight:500;letter-spacing:-0.3px;text-transform:uppercase;line-height:1}
.light{font-family:"Nunito",sans-serif;font-weight:300;line-height:1.25}

.hero-bg{left:0;top:0;width:295px;height:242px;background:radial-gradient(circle at 0 0,#fdf1c0 0%,#fbf5d8 60%,var(--cream) 100%)}
.capacity-panel{left:295px;top:0;width:786px;height:242px;background:var(--teal)}
.left-col{left:0;top:472px;width:288px;height:660px;background:var(--green-pale)}
.center-panel{left:295px;top:472px;width:522px;height:426px;background:var(--teal)}
.right-col{left:826px;top:472px;width:255px;height:653px;background:var(--green-pale)}

.title-energy{left:72px;top:62px;font-family:"Oswald",sans-serif;font-weight:600;font-size:42px;color:var(--orange);line-height:1;letter-spacing:-0.5px}
.title-energy .in-ring{display:inline-block;width:44px;height:44px;border:3px solid var(--orange);border-radius:50%;font-size:28px;text-align:center;line-height:36px;vertical-align:4px;margin-left:4px;font-family:"Nunito",sans-serif;font-weight:800;color:var(--title-green)}
.title-country{left:48px;top:110px;font-family:"Oswald",sans-serif;font-weight:500;font-size:30px;color:var(--title-green);line-height:1;letter-spacing:0.5px}

.banner-capacity{left:326px;top:16px;width:232px;height:29px;background:var(--navy);color:var(--yellow);font-size:17px;padding:6px 10px}
.gears{left:550px;top:6px;width:95px;height:46px}
.bar-label{color:var(--white);font-size:14px}
.bar-caption{color:var(--white);font-size:14px}
.bar-current{left:335px;top:130px;width:37px;height:56px;background:var(--navy)}
.bar-planned{left:418px;top:83px;width:37px;height:103px;background:var(--navy)}
.divider-v{width:1px;background:rgba(255,255,255,.35)}
.bar-solar{left:519px;top:117px;width:38px;height:54px;background:var(--orange)}
.sun-icon{left:556px;top:100px;width:30px;height:30px}
.peak-box{left:627px;top:69px;width:118px;height:84px;text-align:center;color:var(--white);padding-top:8px}
.peak-box .big{font-family:"Oswald",sans-serif;font-size:34px;font-weight:500;line-height:1}
.peak-box .big small{font-size:22px}
.peak-box .light{font-size:12.5px;line-height:1.1;margin-top:2px}
.flag{left:799px;top:144px;width:38px;height:27px}
.solar-note{color:var(--orange);font-size:12.5px;line-height:1.15}
.nuclear-icon{left:946px;top:72px;width:38px;height:38px;border-radius:50%;background:var(--orange)}
.nuclear-text{color:var(--white);font-size:14.5px;line-height:1.2}

.banner-consumption{left:25px;top:261px;width:240px;height:29px;background:var(--navy);color:var(--orange);font-size:17px;padding:6px 0 0 26px;clip-path:polygon(0 0,100% 0,96% 50%,100% 100%,0 100%,4% 50%)}
.consumption-note{left:52px;top:300px;font-size:13.5px;color:#3a3a4a}
.chart-consumption{left:18px;top:325px;width:300px;height:130px}
.peak-tag{left:108px;top:347px;width:72px;height:53px;background:var(--orange);color:var(--white);text-align:center;padding-top:4px;border-radius:2px}
.peak-tag .light{font-size:11px;line-height:1;color:var(--yellow-soft)}
.peak-tag .cond{font-size:19px;color:var(--white);margin-top:4px}
.warning{left:328px;top:257px;width:48px;height:44px}
.warning-note{left:387px;top:264px;color:var(--orange);font-size:13.5px;line-height:1.15}
.times-higher{left:339px;top:341px;color:var(--orange);font-size:21px}
.dots{left:362px;top:364px;width:190px;height:60px}
.expected{left:621px;top:262px;color:var(--orange);font-size:18px}
.triangle-60{left:619px;top:297px;width:157px;height:82px}
.big-60{left:619px;top:333px;width:157px;text-align:center;color:var(--yellow);font-size:36px}
.in-2023{left:638px;top:384px;color:var(--orange);font-size:46px;font-weight:500}
.invest-box{left:855px;top:284px;width:182px;height:140px}
.invest-label{left:855px;top:302px;width:182px;text-align:center;color:var(--white);font-size:18px}
.invest-figure{left:868px;top:330px;color:var(--white);font-size:30px;font-weight:500}
.invest-figure b{font-size:50px;font-weight:500}

.notch{width:0;height:0;border-left:12px solid transparent;border-right:12px solid transparent}
.gov-title{left:295px;top:492px;width:522px;text-align:center;color:var(--white);font-size:21px;font-weight:400}
.building{left:346px;top:531px;width:52px;height:90px;background:var(--orange);border-radius:2px}
.ribbon{left:383px;top:598px;width:382px;height:26px;background:var(--orange);clip-path:polygon(0 0,96% 0,100% 100%,0 100%)}
.ribbon-text{left:460px;top:602px;color:var(--white);font-size:19px;font-weight:400}
.ribbon-text .into{display:inline-block;width:40px;height:40px;border:2px solid var(--yellow);border-radius:50%;text-align:center;line-height:36px;font-size:14px;margin:-10px 2px 0;vertical-align:middle;color:var(--white)}
.ribbon-text .energy{color:var(--yellow)}
.worker{left:380px;top:587px;width:44px;height:44px;border-radius:50%;background:var(--white);border:3px solid var(--orange)}
.big-30{left:437px;top:526px;color:var(--white);font-size:56px;font-weight:400}
.big-30 small{font-size:26px;vertical-align:18px;margin-right:2px}
.tag-construction{left:508px;top:527px;width:189px;height:24px;background:var(--orange);color:var(--yellow);font-size:17px;padding:3px 0 0 6px;clip-path:polygon(0 0,92% 0,100% 100%,0 100%)}
.million{left:515px;top:555px;color:var(--white);font-size:23px;font-weight:400}
.rule-h{height:1px;background:rgba(255,255,255,.3)}
.banner-facility{left:468px;top:677px;width:175px;height:27px;background:var(--orange);color:var(--white);font-size:14px;text-align:center;padding-top:6px;clip-path:polygon(0 0,100% 0,96% 50%,100% 100%,0 100%,4% 50%)}
.num{width:20px;height:20px;border-radius:50%;background:var(--orange);color:var(--white);font-family:"Oswald",sans-serif;font-size:13px;text-align:center;line-height:20px}
.item-title{color:var(--white);font-size:16px;font-weight:400}
.item-value{color:var(--yellow);font-size:21px;font-weight:400}
.item-value small{font-size:13px}
.ybox{background:var(--yellow);color:var(--orange);font-size:14px;padding:4px 0 0 5px;line-height:1}
.ybox.small-text{font-size:12px;line-height:1.05}
.clock{width:40px;height:40px}

.quote{left:24px;top:492px;width:240px;text-align:center;color:var(--orange-deep);font-size:14px;font-weight:400;line-height:1.1}
.quote-by{left:60px;top:525px;width:188px;text-align:right;font-size:13px;color:#333}
.map-area{left:22px;top:571px;width:122px;height:122px;border-radius:6px;background:linear-gradient(160deg,#f3a048 0%,#e9e3b0 45%,#bdbdbd 100%)}
.map-note{left:111px;top:591px;font-size:13.5px;color:var(--ink);line-height:1.15}
.banner-plant{left:57px;top:732px;width:175px;height:28px;background:var(--orange);color:var(--white);font-size:14px;text-align:center;padding-top:7px;clip-path:polygon(0 0,100% 0,96% 50%,100% 100%,0 100%,4% 50%)}
.plant-value{left:75px;top:782px;color:var(--orange-deep);font-size:20px;font-weight:400}
.plant-unit{left:75px;top:805px;color:var(--orange-deep);font-size:13px;font-weight:400}
.chevron{width:50px;height:18px}
.brine-note{left:27px;top:973px;font-size:14px;color:var(--ink);line-height:1.2}
.brine-target{left:61px;top:1023px;color:var(--orange-deep);font-size:16px;font-weight:400}
.waves{left:0;top:1095px;width:288px;height:36px;background:linear-gradient(180deg,#2b8bb0 0%,#1f6f96 100%);border-radius:18px 18px 0 0}

.construction-title{left:324px;top:926px;color:var(--teal);font-size:16px;font-weight:400}
.chart-construction{left:330px;top:960px;width:220px;height:90px}
.tag-orange{background:var(--orange);color:var(--white)}
.tag-10{left:346px;top:979px;width:92px;height:25px;padding:2px 0 0 6px}
.tag-10 .cond{font-size:17px;font-weight:400}
.tag-10 .light{font-size:9.5px;line-height:.95}
.tag-75{left:441px;top:967px;width:90px;height:24px;padding:2px 0 0 5px;font-size:17px;font-weight:400}
.tag-75 small{font-size:12px}
.box-195{left:543px;top:966px;width:193px;height:58px;padding:7px 0 0 12px}
.box-195 .cond{font-weight:400}
.box-195 .amount{font-size:28px}
.box-195 .amount small{font-size:20px}
.box-195 .sub{font-size:13px;color:var(--yellow);margin-top:5px}
.trillion{left:328px;top:1080px;width:457px;height:45px;border-radius:4px 24px 24px 4px;padding:10px 0 0 16px}
.trillion .cond{font-weight:400;font-size:21px}
.trillion .cond small{font-size:14px;color:var(--yellow);margin-left:10px}
.trillion-icon{left:742px;top:1082px;width:41px;height:41px;border-radius:50%;background:var(--white);border:2px solid var(--orange)}

.success-title{left:866px;top:492px;color:var(--teal);font-size:20px;font-weight:400;line-height:1.05}
.chart-success{left:862px;top:545px;width:190px;height:80px}
.demand-arrow{left:862px;top:652px;width:18px;height:80px}
.demand-label{left:885px;top:656px;color:var(--ink);font-size:18px;font-weight:400}
.demand-box{left:882px;top:677px;width:164px;height:46px;background:var(--yellow-soft);padding:10px 0 0 1px;font-size:14px;color:var(--teal);white-space:nowrap}
.demand-box .cond{font-size:19px;color:var(--orange-deep);font-weight:400;margin-left:3px}
.gw-circle{left:912px;top:798px;width:84px;height:84px;border-radius:50%;background:var(--white);border:4px solid var(--orange);text-align:center;color:var(--orange);font-size:24px;font-weight:400;padding-top:25px}
.gw-label{left:896px;top:871px;width:114px;height:22px;background:var(--yellow-soft);text-align:center;font-size:12.5px;padding-top:3px;color:#333}
.saving-box{left:851px;top:966px;width:142px;height:102px;background:var(--orange);color:var(--white);padding:8px 0 0 14px}
.saving-box .light{font-size:17px;margin-left:32px}
.saving-box .amount{font-size:34px;font-weight:400;margin-top:2px}
.saving-box .amount small{font-size:20px}
.saving-box .sub{font-size:17px;font-weight:400;margin-top:4px}
.years-box{left:990px;top:988px;width:72px;height:62px;background:var(--white);border:3px solid var(--orange);border-radius:0 0 8px 0;text-align:center;overflow:hidden}
.years-box .label{font-size:11.5px;color:var(--white);background:var(--orange);padding:1px 0 2px;line-height:1.1}
.years-box .num20{font-size:22px;color:var(--navy);font-weight:400;margin-top:2px}
.years-box .yrs{font-size:12px;color:var(--navy);font-weight:400;margin-top:1px}

.created-by{left:826px;top:1153px;font-size:12px;color:#333}
.brand-name{left:892px;top:1144px;font-family:"Oswald",sans-serif;font-weight:500;font-size:22px;color:var(--teal);line-height:1;letter-spacing:0.2px}
</style>
</head>
<body>
<main class="canvas">
  <div class="hero-bg"></div>
  <div class="capacity-panel"></div>
  <div class="left-col"></div>
  <div class="center-panel"></div>
  <div class="right-col"></div>

  <h1 class="title-energy">ENERGY<span class="in-ring">in</span></h1>
  <h2 class="title-country">SAUDI ARABIA</h2>

  <div class="banner-capacity cond">Energy Generation Capacity</div>
  <svg class="gears" viewBox="0 0 95 46" role="img" aria-label="Gear icons">
    <circle cx="18" cy="30" r="13" fill="#283a8c"/><circle cx="50" cy="26" r="17" fill="#283a8c"/><circle cx="78" cy="14" r="11" fill="#283a8c"/>
  </svg>
  <div class="bar-label cond" style="left:335px;top:111px">55GW</div>
  <div class="bar-current"></div>
  <div class="bar-caption light" style="left:330px;top:190px">Current</div>
  <div class="bar-label cond" style="left:418px;top:63px">120GW</div>
  <div class="bar-planned"></div>
  <svg style="position:absolute;left:418px;top:83px" width="37" height="103" viewBox="0 0 37 103"><path d="M18.5 96V8M8 20l10.5-12L29 20" stroke="#f8ee7c" stroke-width="2.5" fill="none"/></svg>
  <div class="bar-caption light" style="left:418px;top:191px">Planned<br>by 2020</div>
  <div class="divider-v" style="left:501px;top:72px;height:150px"></div>

  <div class="bar-label cond" style="left:522px;top:101px">41GW</div>
  <div class="bar-solar"></div>
  <svg class="sun-icon" viewBox="0 0 30 30"><circle cx="15" cy="15" r="7" fill="#f8ee7c"/><g stroke="#f8ee7c" stroke-width="2"><path d="M15 1v4M15 25v4M1 15h4M25 15h4M5 5l3 3M22 22l3 3M5 25l3-3M22 8l3-3"/></g></svg>
  <svg style="position:absolute;left:617px;top:69px" width="138" height="84" viewBox="0 0 138 84"><path d="M10 0h118v34l10 8-10 8v34H10V50L0 42l10-8z" fill="#f07a2a"/></svg>
  <div class="peak-box">
    <div class="big">OR 30<small>%</small></div>
    <div class="light">Of peak power<br>demand</div>
  </div>
  <div class="bar-label cond" style="left:800px;top:124px">22GW</div>
  <svg class="flag" viewBox="0 0 38 27" role="img" aria-label="Flag of Germany"><rect width="38" height="9" fill="#111"/><rect y="9" width="38" height="9" fill="#dd1c1c"/><rect y="18" width="38" height="9" fill="#f6cc1a"/></svg>
  <div class="solar-note light" style="left:519px;top:177px">Planned solar power<br>generation - 2023</div>
  <svg style="position:absolute;left:644px;top:184px" width="18" height="14" viewBox="0 0 18 14"><path d="M0 7h12M8 2l6 5-6 5" stroke="#f07a2a" stroke-width="3" fill="none"/></svg>
  <div class="solar-note light" style="left:665px;top:177px;width:175px;text-align:right">Almost double current capacity in Germany - the world leader in solar power</div>
  <div class="divider-v" style="left:859px;top:72px;height:150px"></div>

  <div class="nuclear-icon" role="img" aria-label="Nuclear hazard symbol"></div>
  <div class="nuclear-text cond" style="left:882px;top:122px">Saudi Arabia will invest in</div>
  <div class="cond" style="left:881px;top:136px;color:#fff;font-size:46px;font-weight:400">17</div>
  <div class="nuclear-text cond" style="left:922px;top:144px">New nuclear reactors<br>in next 20 years</div>

  <div class="banner-consumption cond">Electricity Consumption</div>
  <p class="consumption-note light">Increased during 1990 to 2010<br>due to economic development</p>
  <svg class="chart-consumption" viewBox="0 0 300 130">
    <path d="M2 113L240 4V113z" fill="#283a8c"/>
    <path d="M126 113V75" stroke="#f8ee7c" stroke-width="1"/>
    <path d="M175 58H297" stroke="#8fa6d0" stroke-width="1"/>
    <text x="4" y="128" font-family="Oswald" font-size="14" fill="#283a8c">1990</text>
    <text x="126" y="128" font-family="Oswald" font-size="14" fill="#283a8c">2001</text>
    <text x="218" y="128" font-family="Oswald" font-size="14" fill="#283a8c">2010</text>
  </svg>
  <div class="peak-tag"><div class="light">Peak loads<br>reached</div><div class="cond">24GW</div></div>

  <svg class="warning" viewBox="0 0 48 44"><path d="M24 2L46 42H2z" fill="#f07a2a"/><rect x="21.5" y="14" width="5" height="16" rx="2" fill="#fff"/><circle cx="24" cy="35.5" r="2.8" fill="#fff"/></svg>
  <p class="warning-note light">There is an urgent need to develop<br>energy conservation policies</p>
  <div class="times-higher cond">25 times higher than in 1975</div>
  <svg class="dots" viewBox="0 0 190 60" fill="#f07a2a">
    <g><circle cx="15" cy="9" r="6"/><circle cx="35" cy="9" r="6"/><circle cx="55" cy="9" r="6"/><circle cx="75" cy="9" r="6"/><circle cx="95" cy="9" r="6"/><circle cx="115" cy="9" r="6"/><circle cx="135" cy="9" r="6"/><circle cx="155" cy="9" r="6"/></g>
    <g><circle cx="8" cy="30" r="6"/><circle cx="28" cy="30" r="6"/><circle cx="48" cy="30" r="6"/><circle cx="68" cy="30" r="6"/><circle cx="88" cy="30" r="6"/><circle cx="108" cy="30" r="6"/><circle cx="128" cy="30" r="6"/><circle cx="148" cy="30" r="6"/><circle cx="168" cy="30" r="6"/></g>
    <g><circle cx="58" cy="50" r="6"/><circle cx="78" cy="50" r="6"/><circle cx="98" cy="50" r="6"/><circle cx="118" cy="50" r="6"/><circle cx="138" cy="50" r="6"/></g>
  </svg>

  <div class="expected cond">Expected to approach</div>
  <svg class="triangle-60" viewBox="0 0 157 82"><path d="M78.5 0L157 82H0z" fill="#f07a2a"/></svg>
  <div class="big-60 cond">60 GW</div>
  <div class="in-2023 cond">IN 2023</div>

  <svg class="invest-box" viewBox="0 0 182 140"><path d="M10 0H182V114H0V10z" fill="#f07a2a"/>
    <g fill="#f07a2a"><circle cx="13" cy="114" r="13"/><circle cx="44" cy="114" r="13"/><circle cx="75" cy="114" r="13"/><circle cx="106" cy="114" r="13"/><circle cx="137" cy="114" r="13"/><circle cx="168" cy="114" r="13"/></g>
    <g font-family="Oswald" font-size="16" fill="#fff" text-anchor="middle"><text x="13" y="121">$</text><text x="44" y="121">$</text><text x="75" y="121">$</text><text x="106" y="121">$</text><text x="137" y="121">$</text><text x="168" y="121">$</text></g>
  </svg>
  <div class="invest-label light">Investment required</div>
  <div class="invest-figure cond">$<b>90</b> BILLION</div>

  <div class="notch" style="left:330px;top:472px;border-top:12px solid var(--cream)"></div>
  <div class="gov-title cond">The government has approved</div>
  <div class="building" role="img" aria-label="Building icon"></div>
  <div class="ribbon"></div>
  <div class="worker" role="img" aria-label="Worker icon"></div>
  <div class="big-30 cond"><small>$</small>30</div>
  <div class="tag-construction cond">The construction of a</div>
  <div class="million cond">Million facility</div>
  <div class="ribbon-text cond">To turn waste <span class="into">INTO</span> <span class="energy">ENERGY</span></div>

  <div class="rule-h" style="left:295px;top:690px;width:522px"></div>
  <div class="banner-facility cond">The facility will</div>

  <div class="num" style="left:327px;top:741px">1</div>
  <div class="item-title cond" style="left:353px;top:743px">Process waste</div>
  <div class="item-value cond" style="left:354px;top:764px">180 <small>TONS</small></div>
  <div class="ybox cond" style="left:354px;top:788px;width:62px;height:56px;padding-top:8px">Per<br>day</div>
  <svg class="clock" style="position:absolute;left:394px;top:797px" viewBox="0 0 40 40"><circle cx="20" cy="20" r="17" fill="#fff" stroke="#f07a2a" stroke-width="4"/><path d="M20 10v11h8" stroke="#f07a2a" stroke-width="3" fill="none"/></svg>

  <div class="num" style="left:485px;top:741px">2</div>
  <div class="item-title cond" style="left:511px;top:743px">Produce</div>
  <div class="item-value cond" style="left:511px;top:764px">6 <small>MW</small></div>
  <div class="ybox cond" style="left:508px;top:788px;width:86px;height:56px;padding-top:12px">Of<br>electricity</div>
  <svg style="position:absolute;left:588px;top:786px" width="30" height="40" viewBox="0 0 30 40"><path d="M13 8a9 9 0 0 1 5 17v5h-9v-5A9 9 0 0 1 13 8z" fill="#f8ee7c" stroke="#f07a2a" stroke-width="2.5"/><rect x="9" y="31" width="9" height="4" fill="#f07a2a"/><path d="M22 4l3-3M26 9l4-1" stroke="#f07a2a" stroke-width="1.5"/></svg>

  <div class="num" style="left:648px;top:741px">3</div>
  <div class="item-title cond" style="left:673px;top:743px">Produce</div>
  <div class="item-value cond" style="left:673px;top:764px">250,000 <small>US GALONS</small></div>
  <div class="ybox cond small-text" style="left:673px;top:788px;width:85px;height:56px;padding-top:7px">(950M3)<br>Of distilled<br>water</div>
  <svg style="position:absolute;left:744px;top:800px" width="24" height="34" viewBox="0 0 24 34"><path d="M12 2C8 12 3 17 3 23a9 9 0 0 0 18 0c0-6-5-11-9-21z" fill="#fff" stroke="#f07a2a" stroke-width="3"/></svg>

  <div class="notch" style="left:330px;top:898px;border-top:12px solid var(--teal)"></div>

  <p class="quote cond">"All power and water plants built from 2020 onwards will run on solar energy"</p>
  <p class="quote-by light">NOVRA's Prince Halvan</p>
  <div class="map-area" role="img" aria-label="Illustration of a sun over a map of Saudi Arabia with a pin at Khafji"></div>
  <p class="map-note light">Saudi Arabia is building the<br>world's largest solar-powered<br>desalination plant at Khafji</p>
  <div class="rule-h" style="left:0;top:745px;width:288px;background:#f4b07a"></div>
  <div class="banner-plant cond">The plant will produce</div>
  <div class="plant-value cond">30,000</div>
  <div class="plant-unit cond">Cubic meters of water</div>
  <svg style="position:absolute;left:200px;top:778px" width="24" height="34" viewBox="0 0 24 34"><path d="M12 2C8 12 3 17 3 23a9 9 0 0 0 18 0c0-6-5-11-9-21z" fill="#fff" stroke="#f07a2a" stroke-width="3"/></svg>
  <div class="ybox cond" style="left:72px;top:821px;width:63px;height:54px;padding-top:8px">Per<br>day</div>
  <svg class="clock" style="position:absolute;left:113px;top:829px" viewBox="0 0 40 40"><circle cx="20" cy="20" r="17" fill="#fff" stroke="#f07a2a" stroke-width="4"/><path d="M20 10v11h8" stroke="#f07a2a" stroke-width="3" fill="none"/></svg>
  <svg class="chevron" style="position:absolute;left:117px;top:927px" viewBox="0 0 50 18"><path d="M0 0h50L25 18z" fill="#f49a4f"/></svg>
  <p class="brine-note light">Coastal Brine Treatment Authority<br><span style="margin-left:34px">needs to increase</span><br><span style="margin-left:34px">desalinated water supply to</span></p>
  <svg style="position:absolute;left:29px;top:995px" width="28" height="36" viewBox="0 0 28 36"><path d="M14 1C9 12 3 18 3 24a11 11 0 0 0 22 0c0-6-6-12-11-23z" fill="#4aa5c9"/></svg>
  <div class="brine-target cond">8.5M cubic metres a day by 2025</div>
  <div class="waves" role="img" aria-label="Decorative wave pattern"></div>

  <div class="construction-title cond">Construction projects in Saudi Arabia</div>
  <svg class="chart-construction" viewBox="0 0 220 90">
    <path d="M7 64L159 48V64z" fill="#1f5e7f"/>
    <path d="M159 30V64" stroke="#1f5e7f" stroke-width="1.5"/>
    <text x="0" y="82" font-family="Nunito" font-size="14" fill="#1f5e7f">2013</text>
    <text x="140" y="82" font-family="Nunito" font-size="14" fill="#1f5e7f">2014</text>
  </svg>
  <div class="tag-10 tag-orange"><span class="cond">10%</span> <span class="light" style="display:inline-block;vertical-align:1px">increase<br>from 2013</span></div>
  <div class="tag-75 tag-orange cond"><small>$</small>75.6 <small>BILLION</small></div>
  <div class="box-195 tag-orange">
    <div class="cond amount"><small>$</small>195.4 <small>BILLION</small></div>
    <div class="cond sub">Planned in the next 3 years</div>
  </div>
  <div class="trillion tag-orange"><div class="cond">$1 TRILLION<small>WORTH OF PROJECTS PLANNED OR UNDER CONSTRUCTION</small></div></div>
  <div class="trillion-icon" role="img" aria-label="Construction worker icon"></div>

  <div class="notch" style="left:933px;top:472px;border-top:12px solid var(--cream)"></div>
  <div class="success-title cond">If energy conservation<br>is successful</div>
  <svg class="chart-success" viewBox="0 0 190 80">
    <path d="M4 72L70 55 100 58 150 40 185 18V76H4z" fill="#f8ee7c"/>
    <path d="M4 66L70 50 100 54 150 34 182 10" stroke="#f07a2a" stroke-width="3" fill="none"/>
    <path d="M170 8l14-2-2 14" stroke="#f07a2a" stroke-width="3" fill="none"/>
  </svg>
  <svg class="demand-arrow" viewBox="0 0 18 80"><path d="M9 0V76M2 66l7 10 7-10" stroke="#f07a2a" stroke-width="2.5" fill="none"/></svg>
  <div class="demand-label cond">Demand</div>
  <div class="demand-box light">Can be reduced<span class="cond">5-10%</span></div>
  <svg class="chevron" style="position:absolute;left:903px;top:752px;width:98px" viewBox="0 0 98 18"><path d="M0 0h98L49 18z" fill="#f49a4f"/></svg>
  <div class="gw-circle cond">3-6 GW</div>
  <div class="gw-label light">Additional capacity</div>
  <svg class="chevron" style="position:absolute;left:903px;top:930px;width:98px" viewBox="0 0 98 18"><path d="M0 0h98L49 18z" fill="#f49a4f"/></svg>
  <div class="saving-box">
    <div class="light">Possible</div>
    <div class="cond amount"><small>$</small>1.5-3.0</div>
    <div class="cond sub">Billion saving</div>
  </div>
  <div class="years-box">
    <div class="light label">Over</div>
    <div class="cond num20">20</div>
    <div class="cond yrs">Years</div>
  </div>

  <div class="created-by light">Created by</div>
  <div class="brand-name">Gulf Powerfair</div>
</main>
</body>
</html>
```